ALL TEXT GRAPHICS RK May 2025 for Instagram

We are looking for a series of social media graphics for Instagram (new size: 4:5 (1080 x 1350 pixels) ratio that are ALL TEXT. We want the following quotes below on each graphic; one quote per graphic. AND, In very small letters at the bottom of each graphic, add @RKBexleyOnline
The look and feel of these graphics should be complimentary to the color palette attached below; but keep them simple. But the design is up to you; at the end of this document, I provided various samples of all text graphics that I like as examples.
women looking to lose weight

```html
<!DOCTYPE html>
<html lang="en">
<head>
<meta charset="UTF-8">
<title>What worked in your 30s won't work now</title>
<link rel="stylesheet" href="https://fonts.googleapis.com/css2?family=Baskervville&family=Poppins:wght@600&display=swap">
<style>
  :root {
    --paper: #ffffff;
    --ink: #111111;
    --accent: #ff369f;
    --on-accent: #ffffff;
  }
  html, body {
    margin: 0;
    padding: 0;
    overflow: hidden;
    background: var(--paper);
  }
  .post {
    position: relative;
    width: 960px;
    height: 1200px;
    background: var(--paper);
    overflow: hidden;
  }
  .bracket {
    position: absolute;
    left: 0;
    top: 0;
  }
  .headline {
    position: absolute;
    left: 89px;
    top: 254px;
    margin: 0;
    font-family: "Baskervville", "Libre Baskerville", serif;
    font-weight: 400;
    font-size: 68px;
    line-height: 86px;
    color: var(--ink);
    letter-spacing: -0.3px;
  }
  .promise {
    position: absolute;
    left: 86px;
    top: 724px;
    margin: 0;
    font-family: "Baskervville", "Libre Baskerville", serif;
    font-weight: 400;
    font-size: 68px;
    line-height: 86px;
    color: var(--ink);
  }
  .promise-band {
    position: absolute;
    left: 89px;
    top: 827px;
    width: 796px;
    height: 133px;
    background: var(--accent);
    box-sizing: border-box;
    padding-left: 44px;
    font-family: "Baskervville", "Libre Baskerville", serif;
    font-size: 90px;
    line-height: 133px;
    color: var(--on-accent);
  }
  .handle {
    position: absolute;
    left: 0;
    width: 960px;
    top: 1128px;
    text-align: center;
    font-family: "Poppins", sans-serif;
    font-weight: 600;
    font-size: 32px;
    line-height: 44px;
    color: var(--accent);
  }
</style>
</head>
<body>
  <main class="post">
    <svg class="bracket" width="960" height="1200" viewBox="0 0 960 1200" aria-hidden="true">
      <path d="M418 205 H88 A36 36 0 0 0 52 241 V527" fill="none" stroke="#ff369f" stroke-width="4"/>
      <polygon points="418,179 449,205 418,231 387,205" fill="#ff369f"/>
      <polygon points="52,497 78,527 52,557 26,527" fill="#ff369f"/>
    </svg>

    <h1 class="headline">What worked in your 30s<br>won’t work now.<br>Here’s what actually does.</h1>

    <p class="promise">Drop 30 pound</p>
    <div class="promise-band">in 3 Months.</div>

    <div class="handle">@RKBexleyOnline</div>
  </main>
</body>
</html>
```